Personal training poster - 1200X900mm

Poster to promote my new personal training service at my gym. The poster will be printed and put into an aframe to be seen by people walking past my gym. It needs to be simple and eye catching with the text i have put in the must haves. The text and image should be the prominent parts of the design.

Target Market(s)

30-50 year old females

Industry/Entity Type

Fitness

Font styles to use
Sans Serif

Requirements
Must have
• my logo
• exercise graphic
• Must include the following text:
• Are you looking for a personal trainer? Our expert trainers can help you achieve you take your health and fitness back!
• Contact details:
• 1300452968
• info@brightmovegym.com.au
• Located under the Harbourview Club

```html
<!DOCTYPE html>
<html lang="en">
<head>
<meta charset="utf-8">
<title>BrightMove Gym – Personal Training Poster</title>
<link href="https://fonts.googleapis.com/css2?family=Oswald:wght@300;400;600;700&display=swap" rel="stylesheet">
<style>
  :root {
    --sky: #2ac6ec;
    --teal: #1a7fa6;
    --deep: #155f86;
    --navy: #1f3f7a;
    --accent: #f8d24c;
    --white: #ffffff;
    --brand-blue: #1f5fa9;
    --skin: #d9a889;
    --kit-grey: #8c8c8c;
    --kit-black: #1c1c24;
  }
  html, body {
    margin: 0;
    padding: 0;
    width: 902px;
    height: 1200px;
    overflow: hidden;
    background: var(--white);
  }
  .poster {
    position: relative;
    width: 902px;
    height: 1200px;
    overflow: hidden;
    background: linear-gradient(100deg, var(--sky) 0%, #22a9d6 45%, var(--teal) 100%);
    font-family: "Oswald", "Arial Narrow", sans-serif;
  }
  .artwork {
    position: absolute;
    inset: 0;
    width: 902px;
    height: 1200px;
  }
  .headline-kicker,
  .headline-main {
    font-family: "Oswald", "Arial Narrow", sans-serif;
    font-weight: 700;
    fill: var(--accent);
  }
  .headline-sub {
    font-family: "Oswald", "Arial Narrow", sans-serif;
    font-weight: 300;
    font-style: italic;
    fill: var(--accent);
  }
  .brand {
    position: absolute;
    left: 34px;
    top: 34px;
    width: 222px;
    display: flex;
    flex-direction: column;
    align-items: center;
    gap: 10px;
  }
  .brand-mark {
    width: 70px;
    height: 70px;
    border-radius: 50%;
    background: var(--brand-blue);
  }
  .brand-name {
    font-family: "Oswald", "Arial Narrow", sans-serif;
    font-weight: 600;
    font-size: 27px;
    letter-spacing: 1px;
    color: var(--brand-blue);
    text-transform: uppercase;
    line-height: 1;
  }
  .contact-list {
    position: absolute;
    left: 66px;
    top: 966px;
    margin: 0;
    padding: 0;
    list-style: none;
  }
  .contact-item {
    display: flex;
    align-items: center;
    height: 40px;
    margin-bottom: 40px;
    color: var(--white);
    font-family: "Oswald", "Arial Narrow", sans-serif;
    font-weight: 300;
    font-size: 21px;
    letter-spacing: 0.3px;
  }
  .contact-icon {
    width: 30px;
    height: 30px;
    margin-right: 22px;
    flex: none;
  }
</style>
</head>
<body>
<main class="poster">
  <svg class="artwork" viewBox="0 0 806 1072" preserveAspectRatio="none" xmlns="http://www.w3.org/2000/svg">
    <defs>
      <linearGradient id="echo-figure-tone" x1="0" y1="0" x2="1" y2="1">
        <stop offset="0" stop-color="#2a4f8f" stop-opacity="0.55"/>
        <stop offset="0.6" stop-color="#1f7aa8" stop-opacity="0.35"/>
        <stop offset="1" stop-color="#1e3f7e" stop-opacity="0.55"/>
      </linearGradient>
      <linearGradient id="athlete-tone" x1="0" y1="0" x2="0" y2="1">
        <stop offset="0" stop-color="#3a2a26"/>
        <stop offset="0.18" stop-color="#d9a889"/>
        <stop offset="0.3" stop-color="#1c1c24"/>
        <stop offset="0.45" stop-color="#d9a889"/>
        <stop offset="0.55" stop-color="#8c8c8c"/>
        <stop offset="0.75" stop-color="#d9a889"/>
        <stop offset="1" stop-color="#1c1c24"/>
      </linearGradient>
    </defs>

    <!-- large tinted background figure -->
    <rect class="photo-echo" role="img" aria-label="Large blue-tinted photo of a woman in sportswear mid-stride, filling the background"
          x="90" y="0" width="660" height="1010" rx="40" fill="url(#echo-figure-tone)"/>

    <!-- upper frame -->
    <polyline points="250,47 748,47 748,205 70,398" fill="none" stroke="var(--accent)" stroke-width="3"/>

    <!-- foreground athlete -->
    <rect class="photo-athlete" role="img" aria-label="Photo of a woman in a black sports bra, grey shorts and trainers doing a high-knee jump"
          x="230" y="112" width="330" height="950" rx="60" fill="url(#athlete-tone)" opacity="0.9"/>

    <!-- lower frame -->
    <polyline points="745,398 60,585 60,812 725,812" fill="none" stroke="var(--accent)" stroke-width="3"/>

    <!-- accent squares -->
    <g fill="var(--accent)">
      <rect x="535" y="218" width="19" height="19"/>
      <rect x="632" y="265" width="11" height="11"/>
      <rect x="612" y="154" width="6" height="6"/>
      <rect x="210" y="327" width="7" height="7"/>
      <rect x="226" y="248" width="32" height="30" opacity="0.5"/>
      <rect x="567" y="488" width="56" height="56" opacity="0.45"/>
      <rect x="248" y="586" width="52" height="52" fill="#c9c25a" opacity="0.85"/>
      <rect x="280" y="600" width="105" height="105" opacity="0.4"/>
    </g>

    <!-- headline -->
    <g transform="translate(410 440) rotate(-17)">
      <text class="headline-kicker" x="20" y="-87" font-size="40" text-anchor="middle" textLength="395" lengthAdjust="spacingAndGlyphs">ARE YOU LOOKING FOR A</text>
      <text class="headline-main" x="0" y="0" font-size="96" text-anchor="middle" textLength="730" lengthAdjust="spacingAndGlyphs">PERSONAL TRAINER?</text>
      <text class="headline-sub" x="-14" y="52" font-size="22" text-anchor="middle" textLength="715" lengthAdjust="spacingAndGlyphs">Our experts can help you achieve you take your health and fitness back!</text>
    </g>

    <!-- logo panel -->
    <polygon points="0,0 245,0 245,140 0,196" fill="var(--white)"/>
  </svg>

  <div class="brand">
    <div class="brand-mark"></div>
    <div class="brand-name">BrightMove Gym</div>
  </div>

  <ul class="contact-list">
    <li class="contact-item">
      <svg class="contact-icon" viewBox="0 0 24 24" fill="none" stroke="#fff" stroke-width="1.6" stroke-linecap="round" stroke-linejoin="round">
        <path d="M5 3h3l2 5-2.5 1.5a11 11 0 0 0 7 7L16 14l5 2v3a2 2 0 0 1-2 2A16 16 0 0 1 3 5a2 2 0 0 1 2-2z"/>
        <path d="M15 3a6 6 0 0 1 6 6M15 7a2 2 0 0 1 2 2"/>
      </svg>
      1300452968
    </li>
    <li class="contact-item">
      <svg class="contact-icon" viewBox="0 0 24 24" fill="none" stroke="#fff" stroke-width="1.6" stroke-linejoin="round">
        <rect x="2" y="5" width="20" height="14" rx="1"/>
        <path d="M2 6l10 7 10-7"/>
      </svg>
      info@brightmovegym.com
    </li>
    <li class="contact-item">
      <svg class="contact-icon" viewBox="0 0 24 24" fill="none" stroke="#fff" stroke-width="1.6" stroke-linejoin="round">
        <path d="M12 22s-7-7.5-7-13a7 7 0 0 1 14 0c0 5.5-7 13-7 13z"/>
        <circle cx="12" cy="9" r="2.5"/>
      </svg>
      Located under the Harbourview Club
    </li>
  </ul>
</main>
</body>
</html>
```